Bref créative
tri-fold brochures and business card designs
New Bravoline company selling wall panels
marketing material
New company looking for marketing print material for display in retail locations and tradshows.
Home and Garden
Consumers and B2B retailers
tri-fold brochure and business card designs.
Please review website for ideas www.murelune7k.com.
I have most of images as high resolution. I have similar brochure from partner in Australia but would like to diferentiate a little. Be creative.
This image should be used for business card design, I think looks the best, but you will have to play with the black side color and incorporate the logo with contact info.
here is the brochure cover used from our Australia partner but I would like to include same layout of all images but on the inside of brochure, I will need to upload additional 4 designs.
Also I have my own bullet points.
Plimsora logo and my company logo which should be used on back cover to say Plimsora by my company logo..
Plimsora logo
here is Plimsora logo as jpeg, not sure which is needed.
My front cover bullet points
I would like to see how this image could be incorporated on the front cover of brochure where the Logo is positioned..
Try this image on back cover to see how it looks.
Should have my contact info like on website with my company logo. see website.
Images
I would like to see the look of the image boxes look like my catalogue images with the name and tile inset which I will upload
Plimsora tile design images 1 of 2 zip files
Panel inset tiles zip file 2 of 2
I need the 2 page of front side of brochure to have the ecoproduct info from my website www.murelune7k.com

```html
<!DOCTYPE html>
<html lang="en">
<head>
<meta charset="utf-8">
<title>Plimsora by Bravoline – Print Set</title>
<link rel="stylesheet" href="https://fonts.googleapis.com/css2?family=Montserrat:wght@400;600;700&family=Open+Sans:wght@400;600;700&display=swap">
<style>
  :root{
    --stage:#3a3532;
    --charcoal:#2d2e31;
    --charcoal-deep:#1c1c1e;
    --card-dark:#111113;
    --ink-soft:#cfd0d2;
    --white:#ffffff;
    --green:#8cc63f;
    --orange:#e8632a;
  }
  *{box-sizing:border-box;margin:0;padding:0}
  html,body{width:1200px;height:874px;overflow:hidden;background:var(--stage)}
  body{position:relative;font-family:"Open Sans",Arial,sans-serif;color:var(--white)}
  .piece{position:absolute;overflow:hidden;background:var(--charcoal);box-shadow:0 4px 14px rgba(0,0,0,.45)}
  .swoosh{position:absolute;inset:0;width:100%;height:100%}
  .photo{position:absolute}
  .brand{font-family:"Montserrat",Arial,sans-serif;font-weight:600;color:var(--white);letter-spacing:-.5px;white-space:nowrap}
  .tagline{font-family:"Montserrat",Arial,sans-serif;font-weight:600;color:var(--white);white-space:nowrap}
  .eco{font-family:"Montserrat",Arial,sans-serif;font-weight:700;color:var(--green);line-height:1.15}
  .body{font-size:6.4px;line-height:1.45;color:var(--ink-soft)}
  .body p+p{margin-top:5px}
  .heading{font-family:"Montserrat",Arial,sans-serif;font-weight:700;color:var(--white)}
  .company-name{position:absolute;font-family:"Montserrat",Arial,sans-serif;font-weight:600;color:var(--white);white-space:nowrap}

  .outside{left:96px;top:43px;width:533px;height:389px}
  .outside .panel{position:absolute;top:0;width:178px;height:389px}
  .outside .p1{left:0}.outside .p2{left:178px;background:#35363a}.outside .p3{left:356px}
  .bamboo{background:linear-gradient(90deg,#6f8f2a,#b7c94a 30%,#5d7a22 55%,#c8d25a 80%,#7d9a33)}
  .fold{position:absolute;top:0;width:1px;height:100%;background:rgba(255,255,255,.12)}
  .bullets{position:absolute;list-style:none;color:var(--white);background:rgba(45,46,49,.88);padding:6px}

  .inside{left:96px;top:444px;width:533px;height:384px}
  .thumbs{position:absolute;left:14px;bottom:12px;display:flex;gap:5px}
  .thumbs div{width:30px;height:30px;background:linear-gradient(135deg,#f4f4f4,#b9b9b9)}

  .front{left:643px;top:43px;width:353px;height:389px}

  .card{left:643px;width:353px;height:91px}
  .card-front{top:629px;background:var(--charcoal-deep)}
  .card-back{top:727px;background:var(--card-dark)}
  .contact{position:absolute;left:190px;top:12px;font-size:6.4px;line-height:1.5;color:var(--ink-soft)}
  .contact .name{font-family:"Montserrat",Arial,sans-serif;font-size:10px;font-weight:600;color:var(--white)}
  .contact .role{font-size:7.5px;color:var(--white);margin-bottom:6px}
</style>
</head>
<body>

<section class="piece outside">
  <div class="panel p1">
    <div class="photo bamboo" role="img" aria-label="Bamboo stalks photograph" style="left:0;top:0;width:178px;height:110px"></div>
    <svg class="swoosh" viewBox="0 0 178 389" aria-hidden="true"><path d="M0 92 C50 140 110 70 178 104 L178 122 C110 92 55 160 0 118 Z" fill="#fff"/></svg>
    <div class="eco" style="position:absolute;left:12px;top:132px;font-size:11px">Eco-friendly<br>Wall covering</div>
    <div class="body" style="position:absolute;left:12px;top:168px;width:154px">
      <p>Our panels are made from renewable plant fibre left over from sugar cane processing, giving every wall a natural, sculpted finish.</p>
      <p>Each design is lightweight, easy to install and can be painted to suit any room, from homes to hotels and shops.</p>
      <p>Paintable, recyclable and free of harmful solvents, the range brings texture and depth to living and working spaces.</p>
    </div>
  </div>
  <div class="panel p2">
    <div class="photo" role="img" aria-label="Close-up of white sculpted wall panel" style="left:0;top:0;width:178px;height:150px;background:linear-gradient(160deg,#9fa1a4,#5b5d61)"></div>
    <svg class="swoosh" viewBox="0 0 178 389" aria-hidden="true"><path d="M0 120 C60 175 120 110 178 150 L178 170 C120 130 60 200 0 142 Z" fill="#fff"/></svg>
    <div class="company-name" style="left:30px;top:200px;font-size:15px">Bravoline</div>
    <div class="body" style="position:absolute;left:30px;top:240px;width:130px">
      Bravoline Inc.<br>Unit 4, 18 Harlow Street<br>Oakridge, ON L4K 2P9<br>T: 905 555 0142<br>info@murelune7k.com
    </div>
    <div style="position:absolute;left:0;width:178px;top:352px;text-align:center;font-size:8px;font-weight:600">www.murelune7k.com</div>
  </div>
  <div class="panel p3">
    <div class="brand" style="position:absolute;left:14px;top:14px;font-size:24px">Plimsora</div>
    <div class="tagline" style="position:absolute;right:12px;top:66px;font-size:10px">Bring Your Walls to Life</div>
    <div class="photo" role="img" aria-label="Orange chair in front of white 3D wall panels" style="left:0;top:92px;width:178px;height:297px;background:linear-gradient(90deg,#e9e9ea 0,#d9d9db 55%,#e8632a 56%,#c44d1c 100%)"></div>
    <svg class="swoosh" viewBox="0 0 178 389" aria-hidden="true"><path d="M0 86 C50 120 120 80 178 100 L178 112 C120 95 60 135 0 104 Z" fill="#fff"/></svg>
    <ul class="body bullets" style="left:10px;top:140px;width:90px">
      <li>• Made from 100% natural plant fibre</li>
      <li>• Biodegradable and fully recyclable</li>
      <li>• Paintable to match any colour scheme</li>
      <li>• Easy to cut, fit and install</li>
    </ul>
  </div>
  <div class="fold" style="left:178px"></div><div class="fold" style="left:356px"></div>
</section>

<section class="piece inside">
  <div class="photo" role="img" aria-label="Living room with white 3D wall panels, orange chair and lamp" style="left:0;top:0;width:533px;height:260px;background:linear-gradient(90deg,#8a7a68 0,#d9d7d3 35%,#f0efed 55%,#e8632a 75%,#6b6a68 100%)"></div>
  <svg class="swoosh" viewBox="0 0 533 384" aria-hidden="true">
    <path d="M0 0 L230 0 C160 40 90 30 0 80 Z" fill="#2d2e31"/>
    <path d="M0 80 C90 30 160 40 230 0 L260 0 C170 55 100 45 0 100 Z" fill="#fff"/>
    <path d="M0 260 C120 220 240 270 533 240 L533 384 L0 384 Z" fill="#2d2e31"/>
    <path d="M0 250 C120 210 240 262 533 232 L533 242 C240 272 120 222 0 262 Z" fill="#fff"/>
  </svg>
  <div class="heading" style="position:absolute;left:14px;top:268px;font-size:11px">About Us</div>
  <div class="body" style="position:absolute;left:14px;top:284px;width:250px">
    <p>Bravoline wall panels are designed to give walls new depth with a sculpted, eco-friendly surface that is simple to install and paint.</p>
    <p>Our collection covers modern, organic and geometric patterns for feature walls, ceilings and retail displays.</p>
  </div>
  <div class="thumbs" role="img" aria-label="Row of tile design swatches">
    <div></div><div></div><div></div><div></div><div></div><div></div><div></div><div></div><div></div><div></div><div></div><div></div><div></div><div></div>
  </div>
  <div class="heading" style="position:absolute;right:14px;top:320px;font-size:9px">Our designs</div>
</section>

<section class="piece front">
  <div class="photo bamboo" role="img" aria-label="Bamboo stalks photograph" style="left:0;top:0;width:170px;height:100px"></div>
  <div class="brand" style="position:absolute;left:196px;top:16px;font-size:24px">Plimsora</div>
  <svg class="swoosh" viewBox="0 0 353 389" aria-hidden="true"><path d="M0 88 C100 140 220 60 353 100 L353 118 C220 82 100 160 0 108 Z" fill="#fff"/></svg>
  <div class="eco" style="position:absolute;left:12px;top:124px;font-size:11px">Eco-friendly<br>Wall covering</div>
  <div class="photo" role="img" aria-label="Armchair beside white sculpted wall panels" style="left:0;top:160px;width:170px;height:110px;background:linear-gradient(135deg,#a88a66,#e4e2de 60%,#bdbcb9)"></div>
  <div class="heading" style="position:absolute;left:12px;top:282px;font-size:10px">About Us</div>
  <div class="body" style="position:absolute;left:12px;top:298px;width:150px">Bravoline panels are designed to bring texture and light to any interior. Each panel is shaped from natural fibre and finished by hand.</div>
  <div class="body" style="position:absolute;left:190px;top:140px;width:150px">We supply homeowners, designers and retailers with a growing catalogue of patterns, each ready to paint or leave in its natural white.</div>
  <div class="fold" style="left:176px"></div>
</section>

<section class="piece card card-front">
  <svg class="swoosh" viewBox="0 0 353 91" aria-hidden="true"><path d="M0 0 L210 0 C180 40 200 70 170 91 L160 91 C190 68 170 38 200 0 Z" fill="#fff"/></svg>
  <div class="photo" role="img" aria-label="White 3D wall panel close-up" style="left:205px;top:0;width:148px;height:91px;background:linear-gradient(135deg,#f3f3f3,#bcbcbc)"></div>
  <div class="brand" style="position:absolute;left:14px;top:10px;font-size:20px">Plimsora</div>
  <div class="tagline" style="position:absolute;left:14px;top:44px;font-size:8px">Bring Your Walls to Life</div>
  <div style="position:absolute;left:14px;top:70px;font-size:7px">www.murelune7k.com</div>
</section>

<section class="piece card card-back">
  <div class="company-name" style="left:18px;top:34px;font-size:17px">Bravoline</div>
  <div class="contact">
    <div class="name">Dana Vendrel</div>
    <div class="role">Sales Director</div>
    Unit 4, 18 Harlow Street, Oakridge ON<br>T: 905 555 0142<br>info@murelune7k.com<br>www.murelune7k.com
  </div>
</section>

</body>
</html>
```